Varelto Stationary and Branding Documents

Corporate Identity Branding stationary needed for IT Recruiting Firm.

I already have a Logo, business cards and website. I need to get designs completed for the remaining corporate identity documents.

The documentation should use similar colors as my website and business card. The designs should modern and clean.

http://varelto-example.com/

Target Market(s)

Information Technology Industry

Industry/Entity Type

Information Technology

Colors
3377b5
0255a3
fbee3e
f78f20
f37122
33a6d7
000000
0592cd

Requirements
Must have
• Letter Head
• Folder Design
• PowerPoint Design
• Invoice
• Envelope
Nice to have
• Proposal
• Flyer
• Brochure
Should not have
• Logo
• Business Cards
• Website

```html
<!DOCTYPE html>
<html lang="en">
<head>
<meta charset="utf-8">
<title>Varelto Projects Proposal Cover</title>
<link href="https://fonts.googleapis.com/css2?family=Montserrat:wght@500;600;700&family=Lato:wght@400&display=swap" rel="stylesheet">
<style>
  :root {
    --backdrop: #c8c9cb;
    --paper: #ffffff;
    --brand-blue: #0a579c;
    --charcoal: #333333;
    --accent-orange: #f37122;
    --ink: #1a1a1a;
  }
  html, body {
    margin: 0;
    padding: 0;
    width: 1200px;
    height: 1200px;
    overflow: hidden;
    background: var(--backdrop);
  }
  .canvas {
    position: relative;
    width: 1200px;
    height: 1200px;
  }
  .proposal-cover {
    position: absolute;
    left: 210px;
    top: 49px;
    width: 780px;
    height: 1102px;
    background: var(--paper);
    overflow: hidden;
  }
  .brand {
    position: absolute;
    left: 78px;
    top: 92px;
    display: flex;
    align-items: center;
    gap: 10px;
    font-family: "Montserrat", sans-serif;
    font-weight: 600;
    font-size: 50px;
    line-height: 1;
    color: var(--brand-blue);
    letter-spacing: 0.5px;
  }
  .brand-mark {
    width: 12px;
    height: 12px;
    background: var(--accent-orange);
  }
  .proponent-details {
    position: absolute;
    left: 89px;
    top: 612px;
    margin: 0;
    padding: 0;
    list-style: none;
    font-family: "Lato", sans-serif;
    font-size: 12px;
    color: var(--ink);
    text-transform: uppercase;
  }
  .proponent-details li {
    height: 25.4px;
    line-height: 1;
  }
  .cover-shapes {
    position: absolute;
    left: 0;
    top: 0;
    width: 780px;
    height: 1102px;
  }
  .cover-title {
    position: absolute;
    right: 65px;
    top: 915px;
    text-align: right;
    color: var(--paper);
    font-family: "Montserrat", sans-serif;
  }
  .cover-title .series {
    font-size: 17px;
    font-weight: 600;
    letter-spacing: 0.3px;
    line-height: 1;
  }
  .cover-title .doc-type {
    font-size: 68px;
    font-weight: 700;
    line-height: 1;
    margin-top: 12px;
    letter-spacing: 1px;
  }
  .cover-title .focus {
    font-size: 17px;
    font-weight: 600;
    line-height: 1;
    margin-top: 16px;
  }
</style>
</head>
<body>
<div class="canvas">
  <section class="proposal-cover">
    <div class="brand">
      <span class="brand-name">varelto</span>
      <span class="brand-mark"></span>
    </div>

    <ul class="proponent-details">
      <li>Name of proponent</li>
      <li>Address</li>
      <li>City/Town</li>
      <li>State/Province</li>
      <li>Zip/Postal code</li>
      <li>Country.if applicable</li>
    </ul>

    <svg class="cover-shapes" viewBox="0 0 780 1102" aria-hidden="true">
      <polygon points="0,804 426,844 0,908" fill="var(--charcoal)"/>
      <polygon points="0,908 780,791 780,1102 0,1102" fill="var(--brand-blue)"/>
    </svg>

    <div class="cover-title">
      <div class="series">VARELTO PROJECTS</div>
      <div class="doc-type">PROPOSAL</div>
      <div class="focus">SPECIFY PROJECT FOCUS</div>
    </div>
  </section>
</div>
</body>
</html>
```